BrightLane Driving School

I need a Facebook page for my Driving School. I teach mostly teenagers how to drive in New Hampshire but also do private classes for adults as well. More info can be found at brightlanelessons.com

```html
<!DOCTYPE html>
<html lang="en">
<head>
<meta charset="utf-8">
<title>BrightLane Driving School – Facebook Cover</title>
<link rel="stylesheet" href="https://fonts.googleapis.com/css2?family=Oswald:wght@400;500;600;700&display=swap">
<style>
  :root {
    --cream: #fdf7e4;
    --sun: #f7dc8e;
    --amber: #f2c200;
    --amber-soft: rgba(255, 236, 160, 0.75);
    --road-dark: #3a2306;
    --road-mid: #9a5f0c;
    --road-light: #e3a52a;
    --ink: #1d1d1b;
    --white: #ffffff;
  }
  * { box-sizing: border-box; }
  html, body {
    margin: 0;
    padding: 0;
    width: 1200px;
    height: 527px;
    overflow: hidden;
    background: var(--cream);
  }
  .cover {
    position: relative;
    width: 1200px;
    height: 527px;
    overflow: hidden;
    font-family: "Oswald", sans-serif;
    background: linear-gradient(100deg, var(--cream) 0%, #fbefc6 35%, var(--sun) 60%, #efbd4a 100%);
  }
  .cover__art {
    position: absolute;
    inset: 0;
    width: 1200px;
    height: 527px;
  }
  .brand {
    position: absolute;
    left: 160px;
    top: 206px;
    display: flex;
    align-items: center;
    gap: 14px;
  }
  .brand__dot {
    width: 58px;
    height: 58px;
    border-radius: 50%;
    background: var(--ink);
    flex: none;
  }
  .brand__text {
    display: flex;
    flex-direction: column;
    line-height: 1;
  }
  .brand__name {
    font-size: 26px;
    font-weight: 700;
    color: var(--ink);
    letter-spacing: 0.2px;
  }
  .brand__phone {
    margin-top: 8px;
    font-size: 16px;
    font-weight: 600;
    color: var(--ink);
    letter-spacing: 1.5px;
  }
  .services {
    position: absolute;
    left: 158px;
    top: 329px;
    width: 424px;
    height: 98px;
  }
  .services__backing {
    position: absolute;
    left: 6px;
    top: 6px;
    width: 424px;
    height: 98px;
    background: var(--amber-soft);
  }
  .services__box {
    position: relative;
    width: 424px;
    height: 98px;
    background: var(--amber);
    padding: 9px 0 0 20px;
  }
  .services__list {
    list-style: none;
    margin: 0;
    padding: 0;
  }
  .services__item {
    font-size: 19px;
    font-weight: 600;
    line-height: 27px;
    color: var(--ink);
    text-transform: uppercase;
  }
  .services__item::before {
    content: "•";
    margin-right: 7px;
  }
  .welcome {
    position: absolute;
    left: 541px;
    top: 180px;
    color: var(--white);
    text-transform: uppercase;
    line-height: 1;
  }
  .welcome__intro {
    font-size: 19px;
    font-weight: 600;
    letter-spacing: 0.3px;
  }
  .welcome__title {
    margin: 18px 0 0;
    font-size: 37px;
    font-weight: 600;
    letter-spacing: 0.2px;
  }
  .welcome__tagline {
    margin-top: 12px;
    font-size: 25px;
    font-weight: 500;
    letter-spacing: 0.2px;
  }
</style>
</head>
<body>
  <main class="cover">
    <svg class="cover__art" viewBox="0 0 1200 527" xmlns="http://www.w3.org/2000/svg">
      <defs>
        <linearGradient id="roadGlow" x1="0" y1="0" x2="1" y2="0.3">
          <stop offset="0" stop-color="#c9860f"/>
          <stop offset="0.3" stop-color="var(--road-light)"/>
          <stop offset="0.6" stop-color="var(--road-mid)"/>
          <stop offset="1" stop-color="var(--road-dark)"/>
        </linearGradient>
      </defs>
      <path class="cover__band" fill="var(--amber)"
            d="M372 0 C448 120 498 210 476 330 C462 420 510 490 536 527 L1200 527 L1200 0 Z"/>
      <path class="cover__photo" fill="url(#roadGlow)" role="img"
            aria-label="Photo from a car interior: side mirror and dashboard with a motion-blurred lit tunnel ahead"
            d="M400 0 C470 120 520 210 500 330 C488 420 536 490 562 527 L1200 527 L1200 0 Z"/>
    </svg>

    <div class="brand">
      <span class="brand__dot"></span>
      <div class="brand__text">
        <span class="brand__name">BrightLane Driving School</span>
        <span class="brand__phone">603 555 0148</span>
      </div>
    </div>

    <section class="services">
      <div class="services__backing"></div>
      <div class="services__box">
        <ul class="services__list">
          <li class="services__item">Teenage Group Driver Education</li>
          <li class="services__item">Individual Driver Education</li>
          <li class="services__item">Senior Driver Evaluations</li>
        </ul>
      </div>
    </section>

    <header class="welcome">
      <div class="welcome__intro">Welcome to</div>
      <h1 class="welcome__title">BrightLane Driving School</h1>
      <div class="welcome__tagline">Preparing you for the road</div>
    </header>
  </main>
</body>
</html>
```